Medical group practice

We need a flyer design incorporating the three doctors in the practice, there is a general practitioner, ophthalmologist and an obstetrician & Gynaecologist. see the attached file for the concept. will leave the colour design up to you

Target Market(s)

general public

Industry/Entity Type

Health Care

Colors

Designer to choose colors to be used in the design.

Requirements
Must have
• logos included in attachement

```html
<!DOCTYPE html>
<html lang="en">
<head>
<meta charset="utf-8">
<title>Brightwell Medical – Flyer</title>
<link href="https://fonts.googleapis.com/css2?family=Hind:wght@400;500;600;700&display=swap" rel="stylesheet">
<style>
  :root {
    --red: #e3232f;
    --navy: #1e3050;
    --ink: #2b2b2b;
    --panel: #ffffff;
    --panel-shade: #eceef1;
    --ring: #d9dce1;
  }
  * { margin: 0; padding: 0; box-sizing: border-box; }
  html, body { width: 849px; height: 1200px; overflow: hidden; background: #fff; }
  body { font-family: "Hind", Arial, sans-serif; color: var(--ink); }

  .flyer { position: relative; width: 849px; height: 1200px; overflow: hidden; background: var(--panel); }

  .hero-photo {
    position: absolute; left: 0; top: 0; width: 849px; height: 585px;
    background:
      radial-gradient(ellipse 230px 300px at 660px 330px, #e9d6c8 0%, rgba(233,214,200,0) 70%),
      radial-gradient(ellipse 160px 260px at 460px 380px, rgba(120,180,190,.35) 0%, rgba(120,180,190,0) 70%),
      linear-gradient(90deg, #ffffff 0%, #f6f7f9 35%, #e8edf2 60%, #f3f5f8 100%);
  }

  .brand { position: absolute; left: 69px; top: 286px; }
  .brand-name {
    font-weight: 700; color: var(--red); font-size: 46px; line-height: 48px; letter-spacing: .5px;
  }
  .brand-rule { width: 296px; height: 2px; background: var(--red); margin-top: 8px; }
  .tagline { font-size: 24px; font-weight: 500; color: var(--ink); margin-top: 4px; }

  .service-badge {
    position: absolute; top: 481px; width: 164px; height: 164px; border-radius: 50%;
    background: #fff; border: 2px solid var(--ring);
    display: flex; align-items: center; justify-content: center; text-align: center;
    font-weight: 600; font-size: 17px; line-height: 20px; color: var(--navy); padding: 20px;
  }
  .badge-eye { left: 60px; }
  .badge-gp { left: 343px; }
  .badge-women { left: 606px; }

  .doctors { position: absolute; left: 0; top: 655px; width: 849px; height: 339px; display: flex; }
  .doctor { position: relative; height: 100%; padding-top: 20px; }
  .doctor + .doctor { box-shadow: -6px 0 8px -6px rgba(0,0,0,.18); }
  .doctor-eye { width: 291px; padding-left: 44px; }
  .doctor-gp { width: 271px; padding-left: 23px; }
  .doctor-women { width: 287px; padding-left: 24px; }

  .doctor-name { font-size: 19px; font-weight: 700; color: var(--red); line-height: 22px; }
  .doctor-name .cred { color: var(--ink); font-weight: 400; font-size: 17px; }
  .doctor-role { font-size: 16px; line-height: 21px; margin-top: 6px; }
  .doctor-mail { font-size: 14.5px; line-height: 19px; }

  .service-list { list-style: none; margin-top: 13px; font-size: 17px; line-height: 23px; }
  .service-list li { position: relative; padding-left: 14px; margin-bottom: 6px; }
  .service-list li::before {
    content: ""; position: absolute; left: 0; top: 9px; width: 5px; height: 5px; border-radius: 50%; background: var(--red);
  }
  .care-group { font-size: 16.5px; line-height: 22px; margin-top: 12px; }
  .care-group b { color: var(--red); font-weight: 600; }

  .hours {
    position: absolute; left: 0; top: 994px; width: 849px; height: 57px; background: var(--red);
    color: #fff; font-size: 25.5px; font-weight: 500; line-height: 59px; padding-left: 46px;
  }

  .contact-band { position: absolute; left: 0; top: 1051px; width: 849px; height: 149px; }
  .phone-lines {
    position: absolute; left: 44px; top: 28px; color: #fff; font-size: 19px; line-height: 29px; font-weight: 400;
  }
  .phone-lines b { font-weight: 600; }
  .address { position: absolute; left: 536px; top: 28px; font-size: 20px; line-height: 30px; color: var(--ink); }
  .address .tel { color: var(--red); font-weight: 500; }
</style>
</head>
<body>
<main class="flyer">
  <div class="hero-photo" role="img" aria-label="Photo of a smiling female doctor with a stethoscope in front of blurred medical staff"></div>

  <header class="brand">
    <div class="brand-name">BRIGHTWELL<br>MEDICAL</div>
    <div class="brand-rule"></div>
    <div class="tagline">Your Health is our Priority</div>
  </header>

  <div class="service-badge badge-eye">Clearview Eye Care</div>
  <div class="service-badge badge-gp">Family Care Clinic</div>
  <div class="service-badge badge-women">Ramsaran Women's Health</div>

  <section class="doctors">
    <article class="doctor doctor-eye">
      <h2 class="doctor-name">Dr. Lucinda R. Ortega</h2>
      <p class="doctor-role">MD. Surgeon Ophthalmologist</p>
      <p class="doctor-mail">E. lucinda.eyes@example.com</p>
      <ul class="service-list">
        <li>Eyes disease examination,</li>
        <li>Surgery of Pterygium,</li>
        <li>Cataract,</li>
        <li>Glaucoma,</li>
        <li>Emergency: Conjunctivitis, Traumatism, Foreign body and more</li>
      </ul>
    </article>

    <article class="doctor doctor-gp">
      <h2 class="doctor-name">Dr. Marcus Holloway, <span class="cred">MD.</span></h2>
      <p class="doctor-role">General Practitioner</p>
      <p class="doctor-mail">E marcus.holloway.md@example.com</p>
      <ul class="service-list">
        <li>General Checks</li>
        <li>Annual Check ups</li>
        <li>Wound Care/Dressings</li>
        <li>Incision &amp; Drainage</li>
        <li>Suturing lacerations</li>
        <li>Pain Injections</li>
        <li>Glucose checks</li>
      </ul>
    </article>

    <article class="doctor doctor-women">
      <h2 class="doctor-name">Dr. Devan Ramsaran <span class="cred">BMedSci, MBBS, DM (O&amp;G), FACOG</span></h2>
      <p class="doctor-role">Obstetrician &amp; Gynaecologist</p>
      <p class="doctor-mail">E. drramsaran@example.com</p>
      <p class="care-group"><b>Obstetrics:</b> Prenatal Care, Delivery, Postnatal checks, High Risk pregnancy</p>
      <p class="care-group"><b>Gynaecology:</b> Pap smears, Abnormal vaginal bleeding, Fibroids, Colposcopy, Family planning, Infertility, Cancer screening,</p>
    </article>
  </section>

  <div class="hours">Opening hours : Monday - Fridays 9am-6pm, Saturdays 10am - 5pm</div>

  <footer class="contact-band">
    <svg width="849" height="149" viewBox="0 0 849 149" aria-hidden="true">
      <polygon points="0,0 505,0 470,149 0,149" fill="var(--navy)"/>
    </svg>
    <div class="phone-lines">
      <div><b>General Practitioner</b> - (555) 014 2231</div>
      <div><b>Ophthalmologist</b> - (555) 014 7780</div>
      <div><b>Obstetrician/Gynaecologist</b> - (555) 014 3392,</div>
    </div>
    <div class="address">
      <div>42 Harbour Lane,</div>
      <div>Port Elmsworth</div>
      <div class="tel">Tel : (555) 014 1100 / 1101</div>
    </div>
  </footer>
</main>
</body>
</html>
```